Orrin Funeral Home stationery
Orrin Funeral Home
Professional
Duncan P. Orrin
Funeral Director
41 Larch St.
Alder Cove, ME 04682
and
58 Mill St.
Pine Harbor, ME 04657
207-516-2870 or 207-739-6152
duncan@orrinfuneralhome.example
www.orrinfuneralhome.example
The Pine Harbor address is the 739 phone number
Logo
Funerals - Cremations - Prearrangements
Logo in eps

```html
<!DOCTYPE html>
<html lang="en">
<head>
<meta charset="utf-8">
<title>Orrin Funeral Home Stationery</title>
<link rel="stylesheet" href="https://fonts.googleapis.com/css2?family=Cinzel:wght@400;600&display=swap">
<style>
  :root{
    --navy:#1e3b87;
    --gold-dark:#6e4b2b;
    --gold-mid:#a8845a;
    --gold-light:#e3d2b2;
    --paper:#ffffff;
    --stage:#ffffff;
    --edge:#d9d9d9;
    --ink-light:#f4ead8;
  }
  *{box-sizing:border-box;margin:0;padding:0}
  html,body{width:1200px;height:734px;overflow:hidden;background:var(--stage)}
  body{position:relative;font-family:"Cinzel",serif}
  .sheet{position:absolute;background:var(--paper);box-shadow:0 0 0 1px var(--edge);overflow:hidden}
  .swoosh{position:absolute;left:0;bottom:0;width:100%;display:block}

  .brand{position:absolute;color:var(--navy);font-family:"Cinzel",serif;font-weight:600;line-height:1.05;display:flex;align-items:center;gap:8px;white-space:nowrap}
  .brand-mark{background:var(--navy);flex:none}
  .brand-name span{display:block}
  .brand-name .sub{font-size:.55em;font-weight:400;letter-spacing:1px}

  /* letterhead */
  .letterhead{left:12px;top:24px;width:521px;height:678px}
  .letterhead .brand{left:22px;top:18px;font-size:30px}
  .letterhead .brand-mark{width:14px;height:14px}
  .letterhead .footer-text{position:absolute;left:30px;bottom:26px;color:var(--ink-light);font-size:9.5px;letter-spacing:.3px;line-height:1.6}

  /* business card */
  .business-card{left:590px;top:54px;width:220px;height:118px}
  .business-card .brand{left:10px;top:14px;font-size:14px;gap:5px}
  .business-card .brand-mark{width:8px;height:8px}
  .business-card .person{position:absolute;right:10px;top:14px;text-align:right;color:var(--navy);font-size:8px}
  .business-card .person small{display:block;font-size:5.5px;margin-top:2px}
  .business-card .card-text{position:absolute;left:12px;bottom:9px;color:var(--ink-light);font-size:5px;line-height:1.55}

  /* note card */
  .note-card{left:775px;top:211px;width:219px;height:120px;background:linear-gradient(90deg,var(--gold-dark),var(--gold-light) 55%,var(--gold-mid))}
  .note-card .brand{left:0;right:0;top:34px;justify-content:center;font-size:15px;color:var(--ink-light);gap:5px}
  .note-card .brand-mark{background:var(--ink-light);width:8px;height:8px}
  .note-card .card-text{position:absolute;left:0;right:0;bottom:16px;text-align:center;color:var(--ink-light);font-size:5.5px;line-height:1.5}

  /* envelope */
  .envelope{left:578px;top:360px;width:612px;height:346px}
  .envelope .flap{position:absolute;left:0;top:0;width:100%;height:108px;background:linear-gradient(90deg,var(--gold-dark),var(--gold-light) 55%,var(--gold-mid));box-shadow:0 1px 0 var(--navy)}
  .envelope .flap .brand{left:0;right:0;top:30px;justify-content:center;font-size:20px;color:var(--ink-light);transform:rotate(180deg)}
  .envelope .flap .brand-mark{background:var(--ink-light);width:10px;height:10px}
  .envelope .return .brand{left:22px;top:122px;font-size:26px}
  .envelope .return .brand-mark{width:12px;height:12px}
  .envelope .return-address{position:absolute;left:34px;bottom:20px;color:var(--ink-light);font-size:9px;line-height:1.5}
</style>
</head>
<body>

<section class="sheet letterhead" aria-label="Letterhead">
  <div class="brand"><i class="brand-mark"></i><span class="brand-name"><span>Orrin</span><span class="sub">Funeral Home</span></span></div>
  <svg class="swoosh" viewBox="0 0 521 140" height="140" preserveAspectRatio="none" aria-hidden="true">
    <defs>
      <linearGradient id="goldLetter" x1="0" x2="1">
        <stop offset="0" stop-color="#6e4b2b"/><stop offset=".55" stop-color="#e3d2b2"/><stop offset="1" stop-color="#a8845a"/>
      </linearGradient>
    </defs>
    <path d="M0 40 Q240 -10 521 10 L521 140 L0 140Z" fill="#1e3b87"/>
    <path d="M0 48 Q250 8 521 40 L521 140 L0 140Z" fill="url(#goldLetter)"/>
  </svg>
  <p class="footer-text">41 Larch St. Alder Cove, ME 04682 and 58 Mill St. Pine Harbor, ME 04657<br>Phone: 207-516-2870 or 207-739-6152 &nbsp;·&nbsp; Fax: 207-739-6152<br>Email: duncan@orrinfuneralhome.example &nbsp;|&nbsp; www.orrinfuneralhome.example</p>
</section>

<section class="sheet business-card" aria-label="Business card">
  <div class="brand"><i class="brand-mark"></i><span class="brand-name"><span>Orrin</span><span class="sub">Funeral Home</span></span></div>
  <p class="person">Duncan P. Orrin<small>Funeral Director</small></p>
  <svg class="swoosh" viewBox="0 0 220 62" height="62" preserveAspectRatio="none" aria-hidden="true">
    <defs>
      <linearGradient id="goldCard" x1="0" x2="1">
        <stop offset="0" stop-color="#6e4b2b"/><stop offset=".55" stop-color="#e3d2b2"/><stop offset="1" stop-color="#a8845a"/>
      </linearGradient>
    </defs>
    <path d="M0 18 Q120 10 220 0 L220 62 L0 62Z" fill="#1e3b87"/>
    <path d="M0 22 Q130 20 220 14 L220 62 L0 62Z" fill="url(#goldCard)"/>
  </svg>
  <p class="card-text">41 Larch St. Alder Cove, ME 04682 · 58 Mill St. Pine Harbor, ME 04657<br>207-516-2870 or 207-739-6152<br>duncan@orrinfuneralhome.example</p>
</section>

<section class="sheet note-card" aria-label="Note card">
  <div class="brand"><i class="brand-mark"></i><span class="brand-name"><span>Orrin</span><span class="sub">Funeral Home</span></span></div>
  <p class="card-text">Funerals - Cremations - Prearrangements<br>www.orrinfuneralhome.example</p>
</section>

<section class="sheet envelope" aria-label="Envelope">
  <div class="flap">
    <div class="brand"><i class="brand-mark"></i><span class="brand-name"><span>Orrin</span><span class="sub">Funeral Home</span></span></div>
  </div>
  <div class="return">
    <div class="brand"><i class="brand-mark"></i><span class="brand-name"><span>Orrin</span><span class="sub">Funeral Home</span></span></div>
  </div>
  <svg class="swoosh" viewBox="0 0 612 120" height="120" preserveAspectRatio="none" aria-hidden="true">
    <defs>
      <linearGradient id="goldEnv" x1="0" x2="1">
        <stop offset="0" stop-color="#6e4b2b"/><stop offset=".55" stop-color="#e3d2b2"/><stop offset="1" stop-color="#a8845a"/>
      </linearGradient>
    </defs>
    <path d="M0 34 Q300 -6 612 0 L612 120 L0 120Z" fill="#1e3b87"/>
    <path d="M0 42 Q320 10 612 30 L612 120 L0 120Z" fill="url(#goldEnv)"/>
  </svg>
  <p class="return-address">41 Larch St. Alder Cove,<br>ME 04682 and 58 Mill St.<br>Pine Harbor, ME 04657</p>
</section>

</body>
</html>
```